Business card with logo for a family psychologist

I need a business card for my private practice in the urban Chicago area as a psychologist. I see families and individuals who are going through difficult times - divorce, separation, illness, or trauma. I want to project hopefulness, competence, and caring.

Target Market(s)

Adults, other professionals - such as physicans and lawyers

Industry/Entity Type

Health Care

Contact Information for Business Card

Front should have my name and credentials; back should have location information including my email, phone

Font styles to use
Serif
Decorative
Script

Requirements
Must have
• Unique logo
Should not have
• No pictures or icons of people; no black

```html
<!DOCTYPE html>
<html lang="en">
<head>
<meta charset="utf-8">
<title>Laura Bennett, Ph.D — Business Card</title>
<link rel="stylesheet" href="https://fonts.googleapis.com/css2?family=Pinyon+Script&family=Lora:ital,wght@0,400;1,400&family=Alike&display=swap">
<style>
  :root {
    --backdrop: #232323;
    --card: #ffffff;
    --navy: #274a7e;
    --blue: #365f9c;
    --sky: #6e98cf;
    --ink: #141414;
  }
  * { margin: 0; padding: 0; box-sizing: border-box; }
  html, body {
    width: 1200px;
    height: 900px;
    overflow: hidden;
    background: var(--backdrop);
  }
  .canvas { position: relative; width: 1200px; height: 900px; }

  .card {
    position: absolute;
    left: 270px;
    width: 652px;
    height: 381px;
    background: var(--card);
    border-radius: 22px;
  }
  .card--front { top: 47px; }
  .card--back { top: 463px; }

  .mark-dot {
    position: absolute;
    border-radius: 50%;
    background: var(--blue);
  }
  .card--front .mark-dot {
    width: 110px; height: 110px;
    left: 271px; top: 72px;
  }

  .holder-name {
    position: absolute;
    left: 0; right: 0;
    top: 206px;
    text-align: center;
    color: var(--navy);
    white-space: nowrap;
  }
  .holder-name__script {
    font-family: "Pinyon Script", cursive;
    font-size: 50px;
  }
  .holder-name__credential {
    font-family: "Lora", serif;
    font-size: 27px;
    font-variant: small-caps;
    letter-spacing: 1px;
    margin-left: 6px;
  }
  .holder-title {
    position: absolute;
    left: 0; right: 0;
    top: 280px;
    text-align: center;
    font-family: "Lora", serif;
    font-style: italic;
    font-size: 15px;
    color: var(--sky);
  }

  .card--back .brand {
    position: absolute;
    left: 0; right: 0;
    top: 62px;
    display: flex;
    flex-direction: column;
    align-items: center;
    gap: 18px;
  }
  .card--back .mark-dot {
    position: static;
    width: 150px; height: 150px;
  }
  .brand__name {
    font-family: "Alike", serif;
    font-size: 26px;
    color: var(--navy);
  }

  .contact {
    position: absolute;
    left: 0; right: 0;
    top: 307px;
    text-align: center;
    font-family: "Alike", serif;
    color: var(--ink);
  }
  .contact__line { font-size: 16.5px; line-height: 24px; }
  .contact__label { color: var(--navy); }
  .contact__sep { margin: 0 8px; }
  .contact__address { font-size: 14px; line-height: 20px; }
</style>
</head>
<body>
<main class="canvas">
  <section class="card card--front">
    <div class="mark-dot" aria-hidden="true"></div>
    <h1 class="holder-name">
      <span class="holder-name__script">Laura Bennett,</span><span class="holder-name__credential">Ph.D</span>
    </h1>
    <p class="holder-title">Licensed Clinical Psychologist</p>
  </section>

  <section class="card card--back">
    <div class="brand">
      <div class="mark-dot" aria-hidden="true"></div>
      <p class="brand__name">Laura Bennett</p>
    </div>
    <address class="contact" style="font-style: normal;">
      <p class="contact__line">
        <span class="contact__label">Phone:</span> 312-555-0148<span class="contact__sep">|</span><span class="contact__label">Email:</span> Drlaurabennett@mail.com
      </p>
      <p class="contact__address">240 W. Lakeview Suite 810, Chicago, Illinois 60610</p>
    </address>
  </section>
</main>
</body>
</html>
```